Consulting Group Needs a Graphic Design

We have created a unique, cyclical process to describe our company's philosophy on parenting to our clients. It is provided in the attached file. At the center of the graphic design, which includes all written words on the page, is an image of a gardener that we really like. We found it through a clipart service, but we are not able to trademark it as our own. We would like to create a similar image which includes the female gardener tending the garden, with a trowel in her hand and a watering can at her side. We want the flowers in her garden to be different, just as every child is unique and different within the same family. For more perspective on our company, please visit www.brookvaleguidance.com.
Updates

Project Deadline Extended
Reason: Some of the designers are getting very close to what we want. Due to some unforeseen circumstances, we were unable to give feedback for a couple of days. We would really appreciate your consideration of our request. We are eager to get the design finished to move forward with our branding strategy, so we will be hyper-focused on the project over the coming days. Thank you, Brookvale Family Advisors

Project Deadline Extended
Reason: We would like to give our first choice designer a chance to create a complementary logo to accompany his submission. We have been in communication with this designer.

Industry/Entity Type

Gardener

```html
<!DOCTYPE html>
<html lang="en">
<head>
<meta charset="utf-8">
<title>Every Good Gardener – Brookvale Family Advisors</title>
<link rel="stylesheet" href="https://fonts.googleapis.com/css2?family=Marcellus&family=Arimo:wght@700&display=swap">
<style>
  :root {
    --page: #ffffff;
    --header-green: #004200;
    --box-fill: #ffffff;
    --box-border: #d23a0a;
    --box-text: #0b3d0b;
    --arrow: #d9471a;
    --sky: #7dbcc6;
    --tree-dark: #0d6a3a;
    --lawn: #5fae2e;
    --lawn-deep: #1f6f22;
    --caption: #ffffff;
  }
  * { margin: 0; padding: 0; box-sizing: border-box; }
  html, body {
    width: 1200px; height: 1000px; overflow: hidden;
    background: var(--page);
  }
  .canvas { position: relative; width: 1200px; height: 1000px; }
  .panel {
    position: absolute; left: 70px; top: 162px;
    width: 1057px; height: 680px; overflow: hidden;
  }
  .panel-header {
    height: 78px; background: var(--header-green);
    display: flex; align-items: center; justify-content: center;
  }
  .panel-title {
    font-family: "Marcellus", serif;
    font-weight: 400; font-size: 52px; letter-spacing: 2px;
    color: #ffffff; padding-top: 4px;
  }
  .garden-scene {
    position: absolute; left: 0; top: 78px; width: 1057px; height: 602px;
    background:
      radial-gradient(ellipse 60% 45% at 50% 78%, #8fd14a 0%, var(--lawn) 45%, transparent 80%),
      linear-gradient(180deg, var(--sky) 0%, var(--tree-dark) 22%, #1c7a2c 45%, var(--lawn) 70%, var(--lawn-deep) 100%);
  }
  .cycle { position: absolute; left: 0; top: 0; width: 1200px; height: 1000px; pointer-events: none; }
  .step {
    position: absolute; width: 142px; height: 90px;
    background: var(--box-fill);
    border: 5px solid var(--box-border); border-radius: 14px;
    display: flex; align-items: center; justify-content: center; text-align: center;
    font-family: "Arimo", sans-serif; font-weight: 700; font-size: 18px; line-height: 1.25;
    color: var(--box-text);
  }
  .step--plants   { left: 551px; top: 253px; }
  .step--nurtures { left: 909px; top: 397px; }
  .step--enriches { left: 826px; top: 657px; }
  .step--prunes   { left: 304px; top: 701px; }
  .step--measures { left: 193px; top: 375px; }
  .copyright {
    position: absolute; left: 70px; width: 1070px; top: 806px;
    text-align: center;
    font-family: "Marcellus", serif; font-size: 17px; color: var(--caption);
  }
</style>
</head>
<body>
<main class="canvas">
  <section class="panel">
    <header class="panel-header">
      <h1 class="panel-title">EVERY GOOD GARDENER:</h1>
    </header>
    <div class="garden-scene" role="img" aria-label="Illustration of a red-haired woman kneeling in a backyard garden, planting colourful flowers with a trowel, a watering can beside her, with a house, fence and trees behind"></div>
  </section>

  <svg class="cycle" viewBox="0 0 1200 1000" aria-hidden="true">
    <g fill="none" stroke="var(--arrow)" stroke-width="5" stroke-linecap="round" stroke-linejoin="round">
      <path d="M295 382 C 350 330, 430 305, 512 302"/>
      <polyline points="478,290 514,302 482,318"/>
      <path d="M697 306 C 780 312, 850 335, 895 372"/>
      <polyline points="876,340 896,373 858,372"/>
      <path d="M1000 490 C 1010 540, 1000 590, 982 634"/>
      <polyline points="976,600 981,636 1008,612"/>
      <path d="M824 744 C 720 775, 590 785, 492 772"/>
      <polyline points="524,756 490,772 522,788"/>
      <path d="M304 700 C 220 640, 195 570, 210 492"/>
      <polyline points="188,518 210,490 234,516"/>
    </g>
  </svg>

  <div class="step step--plants">Plants with<br>purpose</div>
  <div class="step step--nurtures">Nurtures</div>
  <div class="step step--enriches">Enriches<br>the soil</div>
  <div class="step step--prunes">Prunes as<br>needed</div>
  <div class="step step--measures">Measures<br>growth</div>

  <p class="copyright">© 2014 Brookvale Family Advisors</p>
</main>
</body>
</html>
```